Bramwell Resources Ltd. - Refreshed business card challenge

A revised, refreshed business card design for my oil and gas company using my existing logo. Feel free to be as creative as you like!

Target Market(s)

bankers, lawyers

Industry/Entity Type

Oil And Gas Exploration

Contact Information for Business Card

See the "Must Haves" section

Font styles to use
Serif
Sans Serif

Colors

Designer to choose colors to be used in the design.

Requirements
Must have
• Existing business logo, name, title, email, phone number, business address
• Neil Hadley, CA, CPA
• Vice President Finance & Chief Financial Officer
• nhadley@bramwellresources-mail.com
• office: (587)555-0142
• cell: (403)555-0187
• 1400, 815 4 Street S.W.
• Calgary, AB
• T2P 4K8
Should not have
• Should not be plain and boring.

```html
<!DOCTYPE html>
<html lang="en">
<head>
<meta charset="utf-8">
<title>Bramwell Resources – Business Card</title>
<link href="https://fonts.googleapis.com/css2?family=Nunito+Sans:ital,wght@0,400;0,600;0,700;0,800;1,400;1,600&display=swap" rel="stylesheet">
<style>
  :root {
    --forest: #004a30;
    --bark: #5a2d16;
    --paper: #ffffff;
    --backdrop: #e9e6e1;
  }
  * { box-sizing: border-box; margin: 0; padding: 0; }
  html, body { width: 1154px; height: 1200px; overflow: hidden; }
  body {
    background: var(--backdrop);
    font-family: "Nunito Sans", "Helvetica Neue", Arial, sans-serif;
    position: relative;
  }
  .card {
    position: absolute;
    left: 97px;
    width: 960px;
    height: 549px;
    overflow: hidden;
    box-shadow: 0 6px 18px rgba(0,0,0,0.18);
  }
  /* Front */
  .card-front { top: 30px; background: var(--paper); }
  .front-logo {
    position: absolute;
    left: 0; right: 0; top: 150px;
    display: flex; align-items: center; justify-content: center; gap: 22px;
  }
  .logo-mark { width: 46px; height: 46px; background: var(--forest); }
  .logo-name {
    color: var(--forest);
    font-weight: 800;
    line-height: 0.95;
  }
  .logo-name .primary { display: block; font-size: 96px; letter-spacing: -2px; }
  .logo-name .secondary { display: block; font-size: 30px; letter-spacing: 7px; text-align: right; }
  .front-rule {
    position: absolute; left: 0; right: 0; top: 425px;
    height: 3px; background: var(--forest);
  }
  .front-band {
    position: absolute; left: 0; right: 0; top: 434px; bottom: 0;
    background: var(--forest);
    display: flex; align-items: center; justify-content: center;
  }
  .website {
    color: var(--paper);
    font-weight: 700;
    font-size: 33px;
    letter-spacing: 0.5px;
    margin-top: -30px;
  }
  /* Back */
  .card-back { top: 621px; background: var(--forest); color: var(--paper); }
  .back-logo {
    position: absolute; left: 90px; top: 215px;
    display: flex; align-items: center; gap: 16px;
  }
  .back-logo .logo-mark { width: 30px; height: 30px; background: var(--paper); }
  .back-logo .logo-name { color: var(--paper); }
  .back-logo .logo-name .primary { font-size: 56px; letter-spacing: -1px; }
  .back-logo .logo-name .secondary { font-size: 17px; letter-spacing: 4px; }
  .divider {
    position: absolute; left: 500px; top: 140px;
    width: 2px; height: 275px; background: var(--paper);
  }
  .contact { position: absolute; left: 540px; top: 138px; }
  .contact-name { font-size: 33px; font-weight: 600; letter-spacing: 0.5px; }
  .contact-name .credentials { font-size: 22px; font-weight: 600; }
  .contact-title { font-style: italic; font-size: 21px; line-height: 1.35; margin-top: 6px; }
  .contact-phones { font-size: 21px; line-height: 1.5; margin-top: 12px; }
  .contact-phones .label { display: inline-block; width: 34px; }
  .contact-email { font-size: 21px; margin-top: 12px; }
  .contact-address { font-size: 21px; line-height: 1.4; margin-top: 12px; }
</style>
</head>
<body>
  <section class="card card-front" aria-label="Business card front">
    <div class="front-logo">
      <span class="logo-mark"></span>
      <div class="logo-name"><span class="primary">Bramwell</span><span class="secondary">RESOURCES</span></div>
    </div>
    <div class="front-rule"></div>
    <div class="front-band"><p class="website">www.bramwellresources-mail.com</p></div>
  </section>

  <section class="card card-back" aria-label="Business card back">
    <div class="back-logo">
      <span class="logo-mark"></span>
      <div class="logo-name"><span class="primary">Bramwell</span><span class="secondary">RESOURCES</span></div>
    </div>
    <div class="divider"></div>
    <div class="contact">
      <p class="contact-name">NEIL HADLEY<span class="credentials">, CA, CPA</span></p>
      <p class="contact-title">Vice President Finance<br>Chief Financial Officer</p>
      <p class="contact-phones"><span class="label">t.</span>(587) 555-0142<br><span class="label">m.</span>(403) 555-0187</p>
      <p class="contact-email">nhadley@bramwellresources-mail.com</p>
      <p class="contact-address">1400, 815 4 Street<br>S.W. Calgary · Alberta · T2P 4K8</p>
    </div>
  </section>
</body>
</html>
```